Your Harbor Agent Website Design

Creative Brief: Website Design for Your Harbor Agent
- Project Overview: Design a website for our new brand, "Your Harbor Agent". Your Harbor Agent is a service that matches clients with the perfect realtor. The primary function of this site is to serve as a lead generation hub, to generate leads of people who are looking to either buy or sell their house and need a great realtor. The site needs to have a very clean, modern design using sites like Tallyquest, Brickwell, Lantern, and Vexomill as an example. The site also needs to have a primary lead capture capability through a multi-step form or questionnaire that indicates if they are buying or selling, and depending on that selection, creates two different flows.

Target Audience:
- Homebuyers and sellers in the Denver area
- Individuals looking for high-quality realtor services
- Users seeking a seamless and professional online & home buying/selling experience

Objectives:
- Create a visually appealing, modern website with a strong emphasis on lead generation.
- Design advanced, multi-step forms for efficient lead capture.
- Ensure the website is user-friendly and optimized for both desktop and mobile devices.

Pages to Design:
Home Page:
- Engaging hero section with a clear call to action and the ability to enter the form flow
- Brief introduction to Your Harbor Agent and its unique value proposition
- Key features & benefits of being matched with a realtor by Your Harbor Agent
- Testimonials and success stories
- Lead capture form

About Page:
- Overview of Your Harbor Agent’s mission and values
- Professional and trust-building imagery

How it Works Page:
- Step-by-step explanation of the matching process (complete the form and we will match you with a realtor)
- Visual aids (icons, graphics) to simplify complex information
- Customer journey map from inquiry to successful match & sale of home
- Lead capture form

Contact Us Page:
- Simple and accessible contact form
- Contact details
- Call to action for immediate inquiries

Blog Template:
- Clean, easy-to-read layout for blog posts, primarily location/neighborhood guides as well as standard blogs
- Sidebar for recent posts, categories, and tags
- Social sharing buttons
- Lead capture form embedded within blog posts

Design Style:
- Modern and professional with a focus on usability
- Clean lines and intuitive navigation
- Use of curved corners and minimal straight lines for a sleek look
- Incorporation of graphic design elements, potentially including 3D and isomorphic design
- Inspired by sites like Tallyquest, Brickwell, Lantern, and Vexomill
Consistent color scheme and typography

Visual References:
- Tallyquest: For its professional and corporate look
- Brickwell and Lantern: For their user-friendly interfaces and modern design
- Vexomill: For its clean and functional layout

Target Market(s)

- Homebuyers and sellers in the Denver area, Individuals looking for high-quality realtor services, Users seeking a seamless and professional home buying/selling experience

Industry/Entity Type

Real Estate

Number of Pages Required

5+ page

Requirements
Must have
• Fully designed website with lead capture functionality based on brief
Nice to have
• Designed in Figma, Starting / Placeholder copy

```html
<!DOCTYPE html>
<html lang="en">
<head>
<meta charset="utf-8">
<title>About Keyvora</title>
<link href="https://fonts.googleapis.com/css2?family=Outfit:wght@300;400;500;600;700;800&display=swap" rel="stylesheet">
<style>
:root{
  --blue:#1d8fe6;
  --blue-light:#46b4ef;
  --navy:#0b2254;
  --ink:#2b3342;
  --ring:#cfe6f8;
  --sky:#e3f1fb;
  --leaf:#eef4c8;
}
*{margin:0;padding:0;box-sizing:border-box}
html,body{width:1200px;height:2888px;overflow:hidden;background:#fff}
body{position:relative;font-family:'Outfit',sans-serif;color:var(--ink)}
.abs{position:absolute}

/* header */
.logo{font-size:33px;font-weight:400;color:#1a1a1a;letter-spacing:-.5px}
.logo b{font-weight:700;color:var(--blue)}
.nav{left:384px;top:42px;display:flex;font-size:16.5px;font-weight:500;color:#1b1b1b}
.nav a{color:inherit;text-decoration:none;padding:0 14px;border-left:1px solid var(--blue);line-height:20px}
.nav a:first-child{border:none;padding-left:0;position:relative}
.nav a:first-child::after{content:"";position:absolute;left:0;right:14px;bottom:-10px;height:2px;background:var(--blue)}
.btn{left:961px;top:35px;width:135px;height:38px;border-radius:19px;background:linear-gradient(90deg,#1670d6,var(--blue-light));color:#fff;font-size:14px;font-weight:600;display:flex;align-items:center;justify-content:center}

/* hero */
.hero-scene{left:0;top:340px;width:1200px;height:345px;background:linear-gradient(180deg,rgba(255,255,255,0) 0%,#eaf4fc 14%,#cfe5f6 34%,#a9d0ee 52%,#c6e0f1 66%,#e4efd2 78%,var(--leaf) 86%,#fff 100%)}
.hero-title{left:118px;top:252px;line-height:1}
.light{color:var(--blue);font-weight:400}
.heavy{color:var(--navy);font-weight:800}
.hero-title .light{font-size:54px}
.hero-title .heavy{font-size:54px;display:block;margin-top:-2px}
.circle-img{border-radius:50%}
.ring{border-radius:50%;border:2px solid var(--ring)}
.house{background:radial-gradient(ellipse at 52% 48%,#ffffff 0%,#f1f3f3 18%,#bfdff7 36%,#62b2ee 62%,#2a8ee4 82%,#1a74cf 100%)}
.house-base{left:600px;top:500px;width:450px;height:80px;border-radius:50%;background:radial-gradient(ellipse at 50% 40%,rgba(60,90,50,.55),rgba(30,40,50,.15) 60%,rgba(255,255,255,0) 75%)}

/* about */
.h2{font-size:43px;line-height:1.15}
.underline{height:3px;width:68px;background:var(--blue)}
.body{font-size:19px;line-height:23.2px;font-weight:300;color:#222}
.body p+p{margin-top:26px}
.agent{background:linear-gradient(90deg,#c4c9cf 0%,#9aa6b4 22%,#4f6a90 42%,#3e5a84 58%,#9ba8b8 78%,#d5d9dd 100%)}

/* cards */
.band{left:0;top:1320px;width:1200px;height:352px;background:linear-gradient(180deg,#fff 0%,#e6ebf3 22%,#d2dbe8 50%,#c2cee0 74%,#e8edf4 90%,#fff 100%)}
.card{top:1232px;width:470px;height:339px;border-radius:12px;text-align:center;padding:30px 46px 0}
.card.mission{left:120px;background:rgba(255,255,255,.97);border:1px solid var(--ring);color:#333}
.card.vision{left:600px;background:linear-gradient(135deg,#1060c6 0%,#2a8fe0 55%,#4bbaf0 100%);color:#fff}
.card h3{font-size:22px;font-weight:700;margin:8px 0 14px;letter-spacing:.2px}
.card.mission h3{color:var(--navy)}
.card p{font-size:14.5px;line-height:19.6px;font-weight:400}
.dot{border-radius:50%}

/* why */
.handshake{background:linear-gradient(160deg,#efe2b8 0%,#d8c49a 22%,#b89575 40%,#8794a6 60%,#2f4366 80%,#1f2c48 100%)}

/* footer */
.skyline{left:0;top:2205px;width:1200px;height:385px;background:linear-gradient(180deg,#fff 0%,#cde8f8 12%,#8fcaf0 26%,#4fa5de 40%,#2b7dbd 52%,#3c9ad3 62%,#8dcbe9 72%,#dcecc0 82%,var(--leaf) 88%,#fff 100%)}
.col{top:2625px;width:1px;height:185px;background:#dde6ee}
.fh{font-size:19px;font-weight:500;color:#111;border-left:2px solid var(--blue);padding-left:8px;line-height:18px}
.fl{font-size:15px;line-height:28.5px;color:#222;list-style:none}
.social{display:flex;gap:8px}
.social span{width:37px;height:37px;border-radius:50%;background:linear-gradient(135deg,#1670d6,var(--blue-light))}
</style>
</head>
<body>

<!-- header -->
<div class="abs logo" style="left:105px;top:30px">Key<b>vora</b></div>
<nav class="abs nav"><a>About Us</a><a>How it works</a><a>Benefits &amp; Features</a><a>Contact Us</a></nav>
<div class="abs btn">Get Started</div>

<!-- hero -->
<div class="abs hero-scene" role="img" aria-label="Soft blue city skyline illustration fading into green hills"></div>
<div class="abs hero-title"><span class="light">About</span><span class="heavy">Keyvora</span></div>
<svg class="abs" style="left:445px;top:320px" width="125" height="50" viewBox="0 0 125 50"><path d="M2 10 C40 0 55 20 70 35 S100 45 118 40" fill="none" stroke="#1d8fe6" stroke-width="1.6" stroke-dasharray="4 4"/><path d="M112 34 L122 38 L114 46 Z" fill="#1d8fe6"/></svg>
<div class="abs ring" style="left:606px;top:150px;width:455px;height:455px"></div>
<div class="abs house-base"></div>
<div class="abs circle-img house" style="left:617px;top:163px;width:433px;height:433px" role="img" aria-label="3D isometric modern white house with rooftop garden on a city block"></div>

<!-- about -->
<div class="abs h2" style="left:112px;top:725px"><span class="light">About </span><span class="heavy" style="font-weight:700">Keyvora</span></div>
<div class="abs underline" style="left:113px;top:786px"></div>
<div class="abs body" style="left:112px;top:816px;width:482px">
<p>Keyvora is your dedicated partner in navigating the complex world of real estate. We leverage cutting-edge technology to connect you with the best agents who are expertly matched to your specific needs. Our focus is on providing a seamless and personalized experience, whether you're buying, selling, or both.</p>
<p>We're committed to making your real estate journey smooth and successful by pairing you with professionals who understand your goals. With Keyvora, you're not just getting a service—you're gaining a trusted ally in achieving your real estate dreams.</p>
</div>
<div class="abs ring" style="left:639px;top:705px;width:465px;height:465px"></div>
<div class="abs ring" style="left:654px;top:720px;width:435px;height:435px;border-width:1px"></div>
<div class="abs circle-img agent" style="left:668px;top:734px;width:406px;height:406px" role="img" aria-label="Portrait of a real estate agent in a blue suit holding a tablet"></div>

<!-- mission & vision -->
<div class="abs band" role="img" aria-label="Faint grey city buildings and tree silhouettes"></div>
<div class="abs dot" style="left:1027px;top:1218px;width:50px;height:50px;background:#0b2a66"></div>
<div class="abs dot" style="left:111px;top:1533px;width:50px;height:50px;background:var(--blue)"></div>
<div class="abs card mission">
<svg width="62" height="62" viewBox="0 0 62 62"><g fill="none" stroke="#0b2254" stroke-width="2.4"><circle cx="28" cy="34" r="22"/><circle cx="28" cy="34" r="13"/><circle cx="28" cy="34" r="4"/><path d="M28 34 L52 10 M46 10 h6 v6" stroke="#1d8fe6"/></g></svg>
<h3>OUR MISSION</h3>
<p>At Keyvora, our mission is to simplify the real estate process by connecting you with the perfect agent who understands your unique needs. We are committed to providing a seamless, personalized experience that ensures you achieve your real estate goals with confidence and ease.</p>
</div>
<div class="abs card vision">
<svg width="62" height="62" viewBox="0 0 62 62"><g fill="none" stroke="#fff" stroke-width="2.2"><path d="M8 33 Q31 10 54 33 Q31 56 8 33Z"/><circle cx="31" cy="33" r="8"/><circle cx="31" cy="33" r="3"/><path d="M31 6v6M31 54v6M14 12l4 4M48 12l-4 4"/></g></svg>
<h3>OUR VISION</h3>
<p>At Keyvora, our vision is to transform the real estate industry by making the process of finding and working with the right agent effortless and accessible for everyone. We aim to set a new standard of excellence in real estate services, where personalized matches and seamless experiences are the norm, and every client feels empowered to achieve their real estate dreams.</p>
</div>

<!-- why choose -->
<div class="abs ring" style="left:93px;top:1757px;width:465px;height:465px"></div>
<svg class="abs" style="left:108px;top:1772px" width="435" height="435" viewBox="0 0 435 435"><path d="M60 80 A205 205 0 0 0 365 370" fill="none" stroke="#2a9be6" stroke-width="9" stroke-linecap="round"/></svg>
<div class="abs circle-img handshake" style="left:123px;top:1787px;width:405px;height:405px" role="img" aria-label="Two people shaking hands beside a small wooden house with a heart"></div>
<div class="abs h2" style="left:609px;top:1775px;line-height:1.12"><span class="light">Why Choose</span><br><span class="heavy">Keyvora</span></div>
<div class="abs underline" style="left:610px;top:1880px"></div>
<div class="abs body" style="left:611px;top:1907px;width:482px;font-size:18.6px">
<p>Choosing the right real estate agent is crucial to your success, and that's where Keyvora shines. Our proprietary matching process ensures you're paired with top agents who are not only experts in your market but also understand your unique needs. We offer a personalized, stress-free experience from start to finish, backed by a commitment to excellence and transparency. With Keyvora, you gain access to a curated network of trusted professionals, dedicated support, and a seamless path to achieving your real estate goals. When you choose Keyvora, you're choosing a partner who is fully invested in your success.</p>
</div>

<!-- skyline -->
<div class="abs skyline" role="img" aria-label="Blue city skyline illustration over green ground"></div>

<!-- footer -->
<div class="abs logo" style="left:122px;top:2622px;font-size:32px">Key<b>vora</b></div>
<p class="abs" style="left:127px;top:2683px;width:245px;font-size:12.5px;line-height:15.5px;color:#1b2a55">Lorem ipsum dolor sit amet, consectetur adipiscing elit, sed do eiusmod tempor incididunt ut labore et dolore</p>
<p class="abs" style="left:128px;top:2763px;font-size:12px;color:#555">© 2024 Keyvora. All Rights Reserved</p>
<div class="abs col" style="left:426px"></div>
<div class="abs col" style="left:658px"></div>
<div class="abs col" style="left:858px"></div>
<div class="abs fh" style="left:473px;top:2632px">Quick links</div>
<ul class="abs fl" style="left:486px;top:2668px"><li>Home</li><li>About Us</li><li>Features</li><li>How it works</li></ul>
<div class="abs fh" style="left:709px;top:2632px">Resources</div>
<ul class="abs fl" style="left:722px;top:2668px"><li>Testimonials</li><li>Blogs</li><li>Why Us</li><li>Contact Us</li></ul>
<div class="abs fh" style="left:918px;top:2632px">Follow Us</div>
<div class="abs social" style="left:921px;top:2668px"><span></span><span></span><span></span><span></span></div>

</body>
</html>
```